Business card for Financial Technology company

Hello! We'd like to create business cards for 4 members of our company. Our company is a financial technology business that provides funding for businesses. We want to give it a VC (venture captal) look and feel. Clean, fresh and minimal but with a flair of artistry. I'll include some samples of cards we like. It would be great if the back of the card was artistic (see sample files 1 and 2) and the front of the card was the business info. The name of the company is Q7 Funding.

```html
<!DOCTYPE html>
<html lang="en">
<head>
<meta charset="utf-8">
<title>Q7 Funding — Business Card</title>
<link href="https://fonts.googleapis.com/css2?family=Montserrat:wght@400;600&display=swap" rel="stylesheet">
<style>
  :root {
    --page: #e9e7e4;
    --navy: #262f72;
    --navy-deep: #232a6b;
    --white: #ffffff;
    --green: #7bb83a;
    --purple: #6a2c91;
    --magenta: #c2268a;
    --pink: #e3356f;
    --red: #e6473c;
    --orange: #f3832a;
    --yellow: #f6c21c;
    --ink: #262f72;
  }
  * { box-sizing: border-box; margin: 0; padding: 0; }
  html, body { width: 1200px; height: 786px; overflow: hidden; }
  body {
    background: var(--page);
    font-family: "Montserrat", Arial, sans-serif;
    position: relative;
  }
  .card {
    position: absolute;
    top: 236px;
    width: 540px;
    height: 314px;
    overflow: hidden;
    box-shadow: 0 6px 18px rgba(0,0,0,0.18);
  }
  .card--front { left: 40px; background: var(--white); }
  .card--back { left: 620px; background: var(--navy); }

  /* front */
  .front__brand {
    position: absolute;
    top: 58px; left: 0; right: 0;
    display: flex; align-items: center; justify-content: center; gap: 12px;
  }
  .brand__dot {
    width: 34px; height: 34px; border-radius: 50%;
    background: var(--magenta);
  }
  .brand__name {
    font-weight: 600; font-size: 30px; color: var(--ink); letter-spacing: 0.5px;
  }
  .front__stripes { position: absolute; left: 0; top: 150px; width: 540px; height: 34px; }
  .front__band {
    position: absolute; left: 0; right: 0; top: 184px; bottom: 0;
    background: var(--navy);
    display: flex; flex-direction: column; align-items: center; justify-content: center;
    gap: 10px; padding-bottom: 18px;
  }
  .contact__line { color: var(--white); font-size: 15px; font-weight: 400; letter-spacing: 0.3px; }

  /* back */
  .back__pattern {
    position: absolute; inset: 0;
    background: linear-gradient(135deg, var(--navy) 0%, #2d2f78 45%, var(--navy-deep) 100%);
  }
  .back__emblem {
    position: absolute; left: 50%; top: 50%;
    width: 190px; height: 190px; margin: -95px 0 0 -95px;
    border-radius: 50%; background: var(--white);
    display: flex; align-items: center; justify-content: center;
  }
  .back__emblem .brand__name { font-size: 26px; }
</style>
</head>
<body>

  <section class="card card--front" aria-label="Business card front">
    <div class="front__brand">
      <span class="brand__dot"></span>
      <span class="brand__name">Q7 Funding</span>
    </div>

    <svg class="front__stripes" viewBox="0 0 540 34" aria-hidden="true">
      <g stroke-width="2">
        <line x1="0" y1="2" x2="540" y2="2" stroke="var(--green)" stroke-width="3"/>
        <line x1="0" y1="7" x2="540" y2="7" stroke="var(--purple)"/>
        <line x1="0" y1="11" x2="540" y2="11" stroke="var(--purple)"/>
        <line x1="0" y1="15" x2="540" y2="15" stroke="var(--magenta)"/>
        <line x1="0" y1="19" x2="540" y2="19" stroke="var(--pink)"/>
        <line x1="0" y1="23" x2="540" y2="23" stroke="var(--red)"/>
        <line x1="0" y1="27" x2="540" y2="27" stroke="var(--orange)"/>
        <line x1="0" y1="31" x2="540" y2="31" stroke="var(--yellow)"/>
      </g>
    </svg>

    <div class="front__band">
      <p class="contact__line">555-014-2760</p>
      <p class="contact__line">hello@q7funding.com</p>
      <p class="contact__line">www.q7funding.com</p>
    </div>
  </section>

  <section class="card card--back" aria-label="Business card back">
    <div class="back__pattern" role="img" aria-label="Scattered pattern of small green, purple and pink squares on navy"></div>
    <div class="back__emblem">
      <span class="brand__name">Q7 Funding</span>
    </div>
  </section>

</body>
</html>
```